We would like a business card that includes our logo on the front and the following information on the back:

Marcus Brill, Owner
Phone: (308) 555-0184
email: mbrillfencing@postvane.com

Marty Brill & Sons Fencing provides the following services:
Barbed wire
Smooth wire
High tensile
Electric

On the bottom of the card please add:
Please call or email Marcus for estimates.

```html
<!DOCTYPE html>
<html lang="en">
<head>
<meta charset="utf-8">
<title>Marty Brill &amp; Sons Fencing – Business Card</title>
<link href="https://fonts.googleapis.com/css2?family=Cinzel:wght@500&family=Montserrat:wght@400;600&display=swap" rel="stylesheet">
<style>
  :root {
    --stage: #3a3430;
    --paper: #ffffff;
    --brown: #7b5539;
    --ink: #2a2420;
    --cream: #f6efe8;
    --rule: #a88a74;
  }
  * { box-sizing: border-box; margin: 0; padding: 0; }
  html, body { width: 1200px; height: 786px; overflow: hidden; }
  body {
    background: var(--stage);
    display: flex;
    align-items: center;
    justify-content: center;
    gap: 40px;
    font-family: "Montserrat", sans-serif;
  }
  .card {
    width: 540px;
    height: 309px;
    position: relative;
    overflow: hidden;
    box-shadow: 0 10px 28px rgba(0,0,0,.45);
  }

  /* Front */
  .card-front { background: var(--paper); }
  .card-front .band {
    position: absolute; left: 0; right: 0; bottom: 0; height: 112px;
    background: var(--brown);
  }
  .card-front .band-rule {
    position: absolute; left: 0; right: 0; bottom: 120px; height: 3px;
    background: var(--brown);
  }
  .wordmark {
    display: flex; flex-direction: column; align-items: center; gap: 8px;
    font-family: "Cinzel", serif; font-weight: 500;
  }
  .wordmark .mark-square {
    width: 14px; height: 14px; background: currentColor;
  }
  .wordmark .name {
    font-size: 25px; letter-spacing: .5px; line-height: 1.1; text-align: center;
  }
  .wordmark .trade {
    font-size: 13px; letter-spacing: 9px; padding: 3px 0 0 9px;
    border-top: 1px solid currentColor; width: 250px; text-align: center;
  }
  .card-front .wordmark {
    position: absolute; top: 38px; left: 0; right: 0; color: var(--ink);
  }
  .contact-row {
    position: absolute; left: 0; right: 0; bottom: 0; height: 112px;
    display: flex; align-items: center; justify-content: center; gap: 26px;
    color: var(--cream);
  }
  .person { text-align: right; }
  .person .person-name {
    font-family: "Cinzel", serif; font-weight: 500; font-size: 24px; letter-spacing: .5px;
  }
  .person .person-role { font-size: 12px; margin-top: 2px; }
  .divider { width: 1px; height: 46px; background: var(--cream); }
  .contact-list { list-style: none; font-size: 13px; line-height: 1.7; }
  .contact-list li { display: flex; align-items: center; gap: 9px; }
  .contact-list svg { width: 12px; height: 12px; fill: var(--cream); flex: none; }

  /* Back */
  .card-back { background: var(--brown); color: var(--cream); }
  .back-body {
    position: absolute; top: 54px; left: 0; right: 0;
    display: flex; align-items: center; justify-content: center; gap: 30px;
  }
  .card-back .wordmark { color: var(--cream); }
  .card-back .wordmark .name { font-size: 21px; }
  .card-back .wordmark .trade { width: 210px; font-size: 11px; }
  .card-back .divider { height: 110px; }
  .services h2 { font-size: 13px; font-weight: 600; margin-bottom: 3px; }
  .services ul { padding-left: 26px; font-size: 12px; line-height: 1.45; }
  .estimate-note {
    position: absolute; left: 0; right: 0; bottom: 52px;
    text-align: center; font-size: 15px; letter-spacing: .3px;
  }
</style>
</head>
<body>
  <section class="card card-front" aria-label="Card front">
    <div class="wordmark">
      <span class="mark-square"></span>
      <span class="name">Marty Brill &amp; Sons</span>
      <span class="trade">Fencing</span>
    </div>
    <div class="band-rule"></div>
    <div class="band"></div>
    <div class="contact-row">
      <div class="person">
        <div class="person-name">Marcus Brill</div>
        <div class="person-role">Owner</div>
      </div>
      <div class="divider"></div>
      <ul class="contact-list">
        <li>
          <svg viewBox="0 0 24 24" aria-hidden="true"><path d="M6.6 10.8a15.1 15.1 0 0 0 6.6 6.6l2.2-2.2a1 1 0 0 1 1-.25 11.4 11.4 0 0 0 3.6.57 1 1 0 0 1 1 1V20a1 1 0 0 1-1 1A17 17 0 0 1 3 4a1 1 0 0 1 1-1h3.5a1 1 0 0 1 1 1c0 1.25.2 2.45.57 3.57a1 1 0 0 1-.25 1z"/></svg>
          (308) 555-0184
        </li>
        <li>
          <svg viewBox="0 0 24 24" aria-hidden="true"><path d="M2 5h20v14H2z M2 5l10 8 10-8" /></svg>
          mbrillfencing@postvane.com
        </li>
      </ul>
    </div>
  </section>

  <section class="card card-back" aria-label="Card back">
    <div class="back-body">
      <div class="wordmark">
        <span class="mark-square"></span>
        <span class="name">Marty Brill &amp; Sons</span>
        <span class="trade">Fencing</span>
      </div>
      <div class="divider"></div>
      <div class="services">
        <h2>Our Services</h2>
        <ul>
          <li>Barbed wire</li>
          <li>Barbed wire</li>
          <li>Smooth wire</li>
          <li>High tensile</li>
          <li>Electric</li>
        </ul>
      </div>
    </div>
    <p class="estimate-note">Please call or email Marcus for estimates</p>
  </section>
</body>
</html>
```